Verostel business card

Business card for sustainable investment company called "Verostel". Verostel is an exchange platform selling carbon credits between buyers and sellers. Carbon Credits are an environmental commodity for reducing global carbon emissions.

the card should obviously have our logo and the theme should be sustainability/environment mixed with a trading platform.

Contact Information for Business Card

Logo, Name, Title, Phone, Email

Colors
0054AA
0677BA
7BADD7
CADEEF
E8F1F8
0094D4
00A9DD
6FCCEA
C7EBF8
E9F6FB
00AB8E
00BBA5
67D7C9
C6EFE9
E9F9F6
59FF00
82FF00
B8FF75
E3FFCB
F4FFEA

```html
<!DOCTYPE html>
<html lang="en">
<head>
<meta charset="UTF-8">
<title>Verostel Business Card</title>
<link href="https://fonts.googleapis.com/css2?family=Montserrat:wght@400;500;600&display=swap" rel="stylesheet">
<style>
  :root {
    --page-bg: #3a3a3a;
    --navy: #0b2850;
    --cyan: #3fe0ec;
    --blue: #2a86f0;
    --white: #ffffff;
    --paper: #f7f7f7;
  }
  * { margin: 0; padding: 0; box-sizing: border-box; }
  html, body {
    width: 1200px; height: 1200px; overflow: hidden;
    background: var(--page-bg);
    font-family: "Montserrat", sans-serif;
  }
  .card {
    position: absolute; left: 150px;
    width: 900px; height: 514px;
    border-radius: 44px; overflow: hidden;
    box-shadow: 0 10px 30px rgba(0,0,0,.45);
  }
  .card-front { top: 60px; background: linear-gradient(180deg, var(--white), var(--paper)); }
  .card-back { top: 626px; background: var(--navy); }
  .front-shape { position: absolute; inset: 0; }
  .front-brand {
    position: absolute; left: 560px; top: 210px;
    display: flex; align-items: center; gap: 18px;
  }
  .brand-square { width: 58px; height: 58px; background: var(--blue); border-radius: 6px; }
  .brand-name { font-weight: 600; font-size: 44px; color: var(--blue); letter-spacing: 1px; }
  .contact {
    position: absolute; left: 90px; top: 250px; color: var(--white);
  }
  .contact-name {
    border-left: 5px solid var(--cyan); padding-left: 14px; margin-bottom: 16px;
  }
  .contact-name h1 { font-weight: 500; font-size: 34px; color: var(--cyan); line-height: 1; }
  .contact-name p { font-size: 19px; letter-spacing: 1px; margin-top: 4px; }
  .contact-line { display: flex; align-items: center; gap: 14px; font-size: 21px; margin-top: 10px; }
  .contact-line svg { width: 24px; height: 24px; flex: none; }
  .back-brand {
    position: absolute; inset: 0;
    display: flex; align-items: center; justify-content: center; gap: 28px;
  }
  .back-brand .brand-square { width: 90px; height: 90px; background: var(--cyan); }
  .back-brand .brand-name { color: var(--white); font-size: 72px; letter-spacing: 3px; text-transform: uppercase; }
</style>
</head>
<body>
  <section class="card card-front">
    <svg class="front-shape" viewBox="0 0 900 514" width="900" height="514">
      <polygon points="0,0 300,0 495,90 520,514 0,514" fill="var(--navy)"/>
      <polyline points="318,-4 505,82 532,518" fill="none" stroke="var(--cyan)" stroke-width="6" stroke-linejoin="round"/>
    </svg>
    <div class="contact">
      <div class="contact-name">
        <h1>FULL NAME</h1>
        <p>POSITION</p>
      </div>
      <div class="contact-line">
        <svg viewBox="0 0 24 24"><path fill="var(--cyan)" d="M6.6 10.8a15 15 0 0 0 6.6 6.6l2.2-2.2a1 1 0 0 1 1-.25 11.4 11.4 0 0 0 3.6.57 1 1 0 0 1 1 1V20a1 1 0 0 1-1 1A17 17 0 0 1 3 4a1 1 0 0 1 1-1h3.5a1 1 0 0 1 1 1c0 1.25.2 2.45.57 3.57a1 1 0 0 1-.25 1z"/></svg>
        <span>(000) 000 0000</span>
      </div>
      <div class="contact-line">
        <svg viewBox="0 0 24 24"><rect x="2" y="5" width="20" height="14" fill="var(--blue)"/><path d="M2 5l10 8 10-8" fill="none" stroke="var(--white)" stroke-width="1.5"/></svg>
        <span>email@company.com</span>
      </div>
      <div class="contact-line">
        <svg viewBox="0 0 24 24" fill="none" stroke="var(--blue)" stroke-width="1.6"><circle cx="12" cy="12" r="10"/><ellipse cx="12" cy="12" rx="4.5" ry="10"/><path d="M2 12h20M4 7h16M4 17h16"/></svg>
        <span>www.company.com</span>
      </div>
    </div>
    <div class="front-brand">
      <div class="brand-square"></div>
      <span class="brand-name">Verostel</span>
    </div>
  </section>

  <section class="card card-back">
    <div class="back-brand">
      <div class="brand-square"></div>
      <span class="brand-name">Verostel</span>
    </div>
  </section>
</body>
</html>
```